Australian Trucking Company Requires Professional Looking Stationary

We require a professional looking stationary design that incorporates our newly designed logo.

Our business, called "Vell Haulage Contracting", provides contracting work, transport and logistics to business in Western Australia particularly with links to the mining sector.

We are a small business looking to expand and our new logo and our new stationary will help develop our brand image in our market place.

Target Market(s)

Businesses and Corporation with links to the Mining Sector

Industry/Entity Type

Small Business

Requirements
Must have
• The letterhead must have the following details:
The new logo

Text saying: "Vell Haulage Pty Ltd (ACN 582 306 917) ATF The Vell Discretionary Trust T/AS"
"ABN 71 840 239 568"
Address "P.O Box 817 Ashbury WA, 6912"
Phone: 08 9172 5840
Email: vellhaul@mailnest.com.au

The text on the letterhead should be editable as the details are likely to change in the near future. Provision should be made for a website address all though one isn't available at the moment.

The styling, layout and font text is entirely up to the designer.

```html
<!DOCTYPE html>
<html lang="en">
<head>
<meta charset="utf-8">
<title>Vell Haulage Contracting – Letterhead</title>
<link rel="stylesheet" href="https://fonts.googleapis.com/css2?family=PT+Sans:wght@400;700&display=swap">
<style>
  :root {
    --backdrop: #2b2b2b;
    --paper: #ffffff;
    --brand-red: #d3121e;
    --brand-deep: #8c1010;
    --text-grey: #6a6a6a;
    --mark-grey: #5a5a5a;
  }
  * { margin: 0; padding: 0; box-sizing: border-box; }
  html, body {
    width: 1018px;
    height: 1200px;
    overflow: hidden;
    background: var(--backdrop);
    font-family: "PT Sans", "Myriad Pro", Arial, sans-serif;
  }
  .letterhead {
    position: absolute;
    left: 45px;
    top: 0;
    width: 928px;
    height: 1200px;
    background: var(--paper);
    overflow: hidden;
  }
  .brand {
    position: absolute;
    left: 44px;
    top: 84px;
    display: flex;
    align-items: center;
    gap: 18px;
  }
  .brand-square {
    width: 74px;
    height: 74px;
    background: var(--mark-grey);
  }
  .brand-name {
    color: var(--brand-red);
    font-weight: 700;
    font-size: 24px;
    line-height: 1;
    white-space: nowrap;
  }
  .contact {
    position: absolute;
    right: 54px;
    top: 66px;
    text-align: right;
    font-size: 13px;
    line-height: 19px;
    color: var(--text-grey);
    font-style: normal;
  }
  .contact .label { color: var(--brand-deep); }
  .website {
    position: absolute;
    right: 54px;
    top: 1162px;
    font-size: 13px;
    line-height: 19px;
    color: var(--brand-deep);
  }
  .footer-band {
    position: absolute;
    left: 0;
    bottom: 0;
    width: 928px;
    height: 13px;
  }
</style>
</head>
<body>
  <main class="letterhead">
    <header>
      <div class="brand">
        <div class="brand-square"></div>
        <div class="brand-name">Vell Haulage Contracting</div>
      </div>
      <address class="contact">
        <div><span class="label">Vell Haulage Pty Ltd</span>&nbsp; (ACN 582 306 917)</div>
        <div>ATF The Vell Discretionary Trust T/AS</div>
        <div><span class="label">ABN</span> 71 840 239 568</div>
        <div>P.O Box 817 Ashbury WA, 6912</div>
        <div><span class="label">P:</span> 08 9172 5840</div>
        <div><span class="label">E.</span> vellhaul@mailnest.com.au</div>
      </address>
    </header>

    <footer>
      <div class="website">www.vellhaulage.com.au</div>
      <svg class="footer-band" viewBox="0 0 928 13" preserveAspectRatio="none" aria-hidden="true">
        <rect x="0" y="0" width="928" height="13" fill="var(--brand-deep)"/>
        <polygon points="700,0 928,0 928,13 692,13" fill="var(--brand-red)"/>
        <polygon points="694,0 700,0 692,13 686,13" fill="#ffffff"/>
      </svg>
    </footer>
  </main>
</body>
</html>
```